Zielgruppe
Autor: Jura Professor
Zielgruppe: Digital- und Gesundheitswirtschaft
Foto des Autors in hoher Auflösung wird nachgereicht
Aufgabenstellung
Anlehnung an Vorschlag (siehe Word Dokument) wäre wünschenswert.
Aber auch völlig neue Vorschläge sind willkommen.
Bitte an dem Formatlayout im Anhang orientieren und Covers mit Vorder- und Rückseite sowie Buchrücken einsenden. Dankeschön.

```html
<!DOCTYPE html>
<html lang="de">
<head>
<meta charset="utf-8">
<title>Datenwandel und Smart Data im Ordnungsraum des Rechts – Buchumschlag</title>
<link href="https://fonts.googleapis.com/css2?family=Bebas+Neue&family=Cinzel:wght@400&family=Arimo:wght@400&display=swap" rel="stylesheet">
<style>
  :root{
    --page:#ffffff;
    --navy:#04203a;
    --blue-glow:#1a7fc9;
    --blue-mid:#0d4f86;
    --cyan:#3fc2e0;
    --gold:#e79a1f;
    --text:#ffffff;
  }
  html,body{margin:0;padding:0;}
  body{width:1200px;height:848px;overflow:hidden;background:var(--page);position:relative;font-family:"Arimo",Arial,sans-serif;}
  .wrap{position:absolute;left:200px;top:192px;width:788px;height:490px;background:var(--navy);overflow:hidden;color:var(--text);}
  .back{position:absolute;left:0;top:0;width:361px;height:490px;}
  .back-title{position:absolute;left:35px;top:21px;font-size:10.4px;margin:0;font-weight:400;white-space:nowrap;}
  .blurb{position:absolute;left:35px;top:48px;width:296px;font-size:6.9px;line-height:8.7px;margin:0;}
  .blurb p{margin:0 0 8.7px;}
  .rule{position:absolute;left:35px;top:222px;width:302px;height:1px;background:var(--gold);}
  .bio-head{position:absolute;left:35px;top:235px;font-size:8.4px;margin:0;font-weight:400;}
  .bio{position:absolute;left:35px;top:254px;width:292px;font-size:8.4px;line-height:10.2px;margin:0;}
  .topics{position:absolute;left:35px;top:327px;font-size:8.4px;line-height:10.2px;margin:0;padding:0;list-style:none;}
  .bio-end{position:absolute;left:35px;top:377px;font-size:8.4px;margin:0;white-space:nowrap;}
  .author-photo{position:absolute;left:254px;top:320px;width:71px;height:53px;background:linear-gradient(135deg,#d9d9d9,#8a8f96 60%,#2d3240);}
  .code-box{position:absolute;left:229px;top:401px;width:116px;height:54px;background:#fcfbfa;}
  .spine{position:absolute;left:361px;top:0;width:51px;height:490px;}
  .spine-title{position:absolute;left:375px;top:43px;writing-mode:vertical-rl;font-family:"Bebas Neue",sans-serif;font-size:12.4px;line-height:14px;margin:0;font-weight:400;white-space:nowrap;}
  .spine-name{position:absolute;left:384px;top:273px;writing-mode:vertical-rl;font-family:"Cinzel",serif;font-size:15.5px;letter-spacing:1.4px;color:var(--gold);margin:0;white-space:nowrap;}
  .front{position:absolute;left:412px;top:0;width:376px;height:490px;background:radial-gradient(circle at 60% 78%,var(--blue-glow) 0%,var(--blue-mid) 30%,var(--navy) 75%);}
  .front-art{position:absolute;left:0;top:170px;width:376px;height:320px;}
  .front-title{position:absolute;left:0;width:376px;top:40px;text-align:center;font-family:"Bebas Neue",sans-serif;font-size:36px;line-height:30px;margin:0;font-weight:400;white-space:nowrap;}
  .sub-rule{position:absolute;height:1px;background:var(--cyan);}
  .subtitle{position:absolute;left:0;width:376px;top:121px;text-align:center;font-family:"Bebas Neue",sans-serif;font-size:17.5px;line-height:17.5px;color:var(--cyan);margin:0;font-weight:400;white-space:nowrap;}
  .front-name{position:absolute;left:0;width:376px;top:186px;text-align:center;font-family:"Cinzel",serif;font-size:22px;line-height:22px;letter-spacing:1.5px;color:var(--gold);margin:0;}
</style>
</head>
<body>
<div class="wrap">
  <section class="back">
    <h2 class="back-title">Datenwandel und Smart Data im Ordnungsraum des Rechts</h2>
    <div class="blurb">
      <p>Einen einfachen Weg durch den digitalen Wandel gibt es nicht. Umso wichtiger ist es, dass Entscheider in Verwaltung, Kliniken und Wirtschaft die hier vorgestellten Leitlinien, Methoden und praktischen Schritte zeitnah und sorgfältig prüfen.<br>Der Band zeigt, dass neue digitale Chancen nur dann genutzt werden können, wenn die rechtlichen Rahmenbedingungen fundiert verstanden werden.</p>
      <p>Der Autor will mit seiner Darstellung verlässliche Regeln und eine klare digitale Struktur fördern, vor allem mit Blick auf das Gesundheitswesen.</p>
      <p>Die Zielgruppen</p>
      <p>Führungskräfte auf unterschiedlichen Hierarchieebenen,<br>Data Scientists, Controller, IT-Spezialisten, Gesundheitsökonomen,<br>Compliance- sowie Datenschutzbeauftragte,<br>Juristen und Fachanwälte,</p>
      <p>die sich gründlich und praxisnah mit den betroffenen Rechtsfragen und neuen Aufgabenfeldern vertraut machen möchten.</p>
    </div>
    <div class="rule"></div>
    <h3 class="bio-head">Der Herausgeber und Autor</h3>
    <p class="bio">Prof. Dr. iur. Gottfried Marwitz forscht und lehrt an Hochschulen in Berlin, Ludwigshafen/ Rhein, Stuttgart sowie an der Donaustein Universität Budapest. Er ist Professor, Visiting Professor und Dozent auf dem Gebiet der Rechtswissenschaften. Seine Forschungsschwerpunkte sowie zahlreiche Publikationen und Vorträge befassen sich insbesondere mit folgenden Themenfeldern:</p>
    <ul class="topics">
      <li>Digitalisierung, Big Data, Analytics und Recht</li>
      <li>Datenschutz- und Datensicherheitsrecht</li>
      <li>Internetrecht, IuK-Recht</li>
      <li>Internationales Recht, Europa- und Wirtschaftsrecht</li>
    </ul>
    <div class="author-photo" role="img" aria-label="Porträtfoto des Autors"></div>
    <p class="bio-end">Prof. Marwitz verfügt über eine breite Projekt- und Gutachtenserfahrung sowie</p>
    <div class="code-box"></div>
  </section>

  <section class="spine"></section>
  <h2 class="spine-title">Datenwandel und Smart Data<br>im Ordnungsraum des Rechts</h2>
  <p class="spine-name">GOTTFRIED MARWITZ</p>

  <section class="front">
    <svg class="front-art" role="img" aria-label="Illustration: Hand aus digitalem Netzwerk berührt eine Weltkugel aus Lichtpunkten" viewBox="0 0 376 320" preserveAspectRatio="none">
      <defs>
        <radialGradient id="glow" cx="0.62" cy="0.56" r="0.6">
          <stop offset="0" stop-color="#4ab8f0" stop-opacity="0.55"/>
          <stop offset="1" stop-color="#0d4f86" stop-opacity="0"/>
        </radialGradient>
      </defs>
      <rect width="376" height="320" fill="url(#glow)"/>
    </svg>
    <h1 class="front-title">Datenwandel und Smart Data<br>im Ordnungsraum des Rechts</h1>
    <div class="sub-rule" style="left:75px;top:118px;width:233px;"></div>
    <p class="subtitle">Für eine klare digitale Struktur am Beispiel<br>des Gesundheitswesens</p>
    <div class="sub-rule" style="left:108px;top:162px;width:156px;"></div>
    <p class="front-name">GOTTFRIED<br>MARWITZ</p>
  </section>
</div>
</body>
</html>
```